Corvale Spine & Joint Business Card

Need a business card using the logo provided. I want brand side of the card to be grey with the logo in the center of the card in white.

On the other side I leave to the designers

Target Market(s)

Personal Injury Attorneys

Industry/Entity Type

Medical

Contact Information for Business Card

Name, CEO. Cell Phone, (Hialeah, Address, Phone) (Homestead, Address, Phone) (Tallahassee, Address, Phone)

Colors

Designer to choose only greyscale colors for use in the design.

Requirements
Must have
• Logo by itself on one side

```html
<!DOCTYPE html>
<html lang="en">
<head>
<meta charset="utf-8">
<title>Corvale Spine &amp; Joint – Business Card</title>
<link href="https://fonts.googleapis.com/css2?family=Montserrat:wght@400;500;700&display=swap" rel="stylesheet">
<style>
  :root {
    --stage: #2f3031;
    --brand-grey: #a5a7a8;
    --contact-grey: #5f6265;
    --ink-white: #ffffff;
    --ink-soft: rgba(255,255,255,0.9);
  }
  * { box-sizing: border-box; margin: 0; padding: 0; }
  html, body { width: 1200px; height: 801px; overflow: hidden; }
  body {
    background: var(--stage);
    font-family: "Montserrat", sans-serif;
    color: var(--ink-white);
    display: flex;
    align-items: center;
    justify-content: center;
    gap: 40px;
  }
  .card {
    width: 540px;
    height: 309px;
    border-radius: 14px;
    position: relative;
    overflow: hidden;
  }
  .card--brand {
    background: var(--brand-grey);
    display: flex;
    align-items: center;
    justify-content: center;
  }
  .card--contact { background: var(--contact-grey); }

  .wordmark {
    font-weight: 500;
    color: var(--ink-white);
    text-align: center;
    line-height: 1;
  }
  .wordmark__name { display: block; font-size: 54px; letter-spacing: 6px; }
  .wordmark__tag { display: block; font-size: 17px; letter-spacing: 7px; margin-top: 6px; }

  .card--contact .wordmark {
    position: absolute;
    top: 24px;
    left: 0;
    right: 0;
  }
  .card--contact .wordmark__name { font-size: 36px; letter-spacing: 5px; }
  .card--contact .wordmark__tag { font-size: 11.5px; letter-spacing: 5px; margin-top: 4px; }

  .person {
    position: absolute;
    top: 96px;
    left: 0;
    right: 0;
    text-align: center;
  }
  .person__name { font-weight: 700; font-size: 16px; letter-spacing: 0.5px; }
  .person__role { font-weight: 500; font-size: 11.5px; margin-top: 2px; }
  .person__phone { font-weight: 500; font-size: 13px; margin-top: 6px; }

  .location {
    position: absolute;
    width: 150px;
    transform: translateX(-50%);
    text-align: center;
    font-size: 10px;
    line-height: 1.35;
    color: var(--ink-soft);
  }
  .location__city { font-weight: 700; font-size: 12px; color: var(--ink-white); }
  .location__phone { font-weight: 700; font-size: 14px; color: var(--ink-white); margin-top: 1px; }
  .location--hialeah { left: 150px; top: 218px; }
  .location--homestead { left: 300px; top: 162px; }
  .location--tallahassee { left: 452px; top: 104px; }
</style>
</head>
<body>
  <section class="card card--brand" aria-label="Brand side">
    <div class="wordmark">
      <span class="wordmark__name">CORVALE</span>
      <span class="wordmark__tag">SPINE &amp; JOINT</span>
    </div>
  </section>

  <section class="card card--contact" aria-label="Contact side">
    <div class="wordmark">
      <span class="wordmark__name">CORVALE</span>
      <span class="wordmark__tag">SPINE &amp; JOINT</span>
    </div>

    <div class="person">
      <p class="person__name">DR. MARCUS HALE</p>
      <p class="person__role">CEO</p>
      <p class="person__phone">0100 555 246</p>
    </div>

    <div class="location location--tallahassee">
      <p class="location__city">TALLAHASSEE</p>
      <p>1450 Palm Crest Ave #310</p>
      <p>Tallahassee, FL 33010</p>
      <p class="location__phone">954-555-0172</p>
    </div>

    <div class="location location--homestead">
      <p class="location__city">HOMESTEAD</p>
      <p>1450 Palm Crest Ave #310</p>
      <p>Homestead, FL 33010</p>
      <p class="location__phone">954-555-0172</p>
    </div>

    <div class="location location--hialeah">
      <p class="location__city">HIALEAH</p>
      <p>1450 Palm Crest Ave #310</p>
      <p>Hialeah, FL 33010</p>
      <p class="location__phone">954-555-0172</p>
    </div>
  </section>
</body>
</html>
```